Brackenford Group Website

We have a newly established brand for a company with an existing portfolio of property. The company is corporate and professional and both owns and develops property. The website should reflect a professional and stable organisation. The website should showcase the existing properties (6), have a home page that describes the company and its activities and has a "about us" page. The website will be in Wordpress and we would like the code for all pages to be sent to us by the successful designer upon completion of the job.
Updates

sorry was called from the office on an urgent matter. To be fair on submitters, i need a couple more days to finalise reviews.

Contact Information for Business Card

Brackenford Logo on front
Black background with silver logo.

Coding

Number of Pages Required

Colors

Designer to choose colors to be used in the design.

Requirements
Must have
• Text side of card should include
• Brackenford Property Group (as title in logo font)
• Employee Name (centered)
• Job Title (centered below name)
• Address 4 lines
• Email, mobile office phone, 3 lines
• website address (probably as footer)

```html
<!DOCTYPE html>
<html lang="en">
<head>
<meta charset="utf-8">
<title>Brackenford Property Group</title>
<link href="https://fonts.googleapis.com/css2?family=Libre+Baskerville&family=Lato:wght@400;700&display=swap" rel="stylesheet">
<style>
:root{
  --accent:#1b8cf2;
  --accent-dark:#0f6fd0;
  --page:#0e0b0d;
  --navy:#0f1824;
  --white:#ffffff;
  --muted:#b9bec6;
  --body-dark:#6d6f73;
  --serif:'Libre Baskerville', Georgia, serif;
  --sans:'Lato', Arial, sans-serif;
}
*{margin:0;padding:0;box-sizing:border-box}
html,body{width:1200px;height:3841px;overflow:hidden}
body{background:var(--page);color:var(--white);font-family:var(--sans);position:relative}
.abs{position:absolute}
a{color:inherit;text-decoration:none}

/* header */
.site-header{left:0;top:0;width:1200px;height:89px;background:#111416;z-index:3;border-bottom:1px solid #24282c}
.brand{display:flex;align-items:center;gap:10px;font-family:var(--serif);font-size:17px;letter-spacing:2px;color:#e8e9eb}
.brand-mark{width:14px;height:14px;border:1.5px solid #e8e9eb}
.site-header .brand{position:absolute;left:161px;top:33px}
.main-nav{position:absolute;left:510px;top:37px;display:flex;gap:26px;font-size:13px;color:#e6e6e6}
.btn-header{position:absolute;left:926px;top:27px;width:113px;height:40px;background:var(--accent);font-family:var(--serif);font-size:14px;display:flex;align-items:center;justify-content:center}

/* hero */
.hero{left:0;top:89px;width:1200px;height:660px;background:
 linear-gradient(180deg,rgba(14,11,13,0) 45%,var(--page) 100%),
 linear-gradient(100deg,#3a2a24 0%,#5a4a44 25%,#2d3a4a 50%,#6a4a3a 75%,#3a2a2a 100%)}
.hero-title{left:0;width:1200px;top:218px;text-align:center;font-family:var(--serif);font-size:44px;line-height:57px;letter-spacing:.5px}
.hero-sub{left:280px;width:640px;top:335px;text-align:center;font-size:13px;line-height:21px;color:#e8e8e8}
.btn-quote{left:507px;top:423px;width:186px;height:53px;background:var(--accent);font-family:var(--serif);font-size:17px;display:flex;align-items:center;justify-content:center}
.vline{width:1px;background:#2c5f8c}
.slider-ctrl{left:160px;top:678px;display:flex;align-items:center;font-size:11px;color:#ddd}
.slider-ctrl .current{color:var(--accent);font-size:18px;margin:0 14px 0 10px}
.dots{position:relative;width:124px;height:1px;background:#888;margin-right:24px}
.dots span{position:absolute;top:-2px;width:5px;height:5px;border-radius:50%;background:#ddd}

/* expertise */
.section-title{font-family:var(--serif);font-size:42px;text-align:center;left:0;width:1200px}
.tabs{left:162px;top:915px;display:flex;gap:27px;font-family:var(--serif);font-size:12px;letter-spacing:.3px}
.tabs .active{color:var(--accent)}
.tile{top:990px;height:337px;background:linear-gradient(160deg,#2f93f5,#0f6fd8)}
.tile-photo{background:linear-gradient(180deg,#9fb0bc 0%,#b8c2c6 45%,#7a6048 70%,#5a4a3a 100%)}
.plus-btn{left:602px;top:1275px;width:76px;height:73px;background:var(--accent)}
.exp-heading{left:704px;top:988px;font-family:var(--serif);font-size:27px;line-height:37px;color:var(--accent)}
.exp-text{left:704px;top:1077px;width:340px;font-size:11.5px;line-height:24px;color:#e0e0e0}
.pager{display:flex;gap:28px;font-family:var(--serif);font-size:11px;letter-spacing:.4px}
.pager span{display:flex;align-items:center;gap:8px}
.tri-l{width:0;height:0;border-top:4px solid transparent;border-bottom:4px solid transparent;border-right:6px solid var(--accent)}
.tri-r{width:0;height:0;border-top:4px solid transparent;border-bottom:4px solid transparent;border-left:6px solid var(--accent)}

/* about */
.about-photo{left:487px;top:1418px;width:713px;height:636px;background:linear-gradient(160deg,#4f7c8e 0%,#8fb0b8 35%,#e4e4e0 60%,#c8c6c0 100%)}
.about-panel{left:0;top:1512px;width:637px;height:448px;background:var(--white);color:#222}
.about-panel h2{position:absolute;left:162px;top:50px;font-family:var(--serif);font-weight:400;font-size:37px}
.about-panel p{position:absolute;left:162px;top:105px;width:430px;font-size:11.5px;line-height:24px;color:var(--body-dark)}
.about-panel .vline{position:absolute;left:189px;top:307px;height:44px;background:#7fb8ee}
.explore{position:absolute;left:162px;top:376px;font-family:var(--serif);font-size:14px;color:var(--accent);display:flex;align-items:center;gap:10px}

/* case studies */
.cases-bg{left:0;top:2054px;width:1200px;height:1196px;background:linear-gradient(180deg,#0d1622 0%,#14202e 40%,#101b28 70%,#0c121a 100%)}
.case-card{top:2197px;width:203px;height:202px;display:flex;flex-direction:column;justify-content:flex-end;align-items:center;padding-bottom:18px;font-family:var(--serif);font-size:14px;text-align:center}
.case-card .caption{position:relative}
.case-1{left:161px;background:linear-gradient(180deg,#1e3a5a 0%,#3a4e62 55%,#0e1622 100%)}
.case-1 .name{font-size:21px;margin-bottom:8px}
.case-1 .addr{font-family:var(--sans);font-size:11px;line-height:19px;color:#ddd}
.case-2{left:386px;background:linear-gradient(180deg,#1a1a1c 0%,#3a3a3c 55%,#111 100%)}
.case-3{left:611px;background:linear-gradient(180deg,#2e6ea8 0%,#5a6e80 55%,#1e2a36 100%)}
.case-4{left:836px;background:linear-gradient(180deg,#6a7a90 0%,#c08a8a 40%,#7a6a62 70%,#1e1a1a 100%)}
.case-detail-title{left:0;width:1200px;top:2508px;text-align:center;font-family:var(--serif);font-size:36px}
.case-detail-text{left:384px;width:432px;top:2564px;text-align:center;font-size:11.5px;line-height:24px;color:#e0e0e0}

/* team */
.team-title{left:162px;top:2918px;font-family:var(--serif);font-size:36px;color:var(--accent)}
.team-text{left:162px;top:2970px;width:225px;font-size:11.5px;line-height:24px;color:#e0e0e0}
.member{width:188px;height:188px;background:var(--white);text-align:center;color:#1b1b1b}
.member .photo{position:absolute;left:6px;top:6px;width:176px;height:113px;background:linear-gradient(180deg,#e6f1fb,#cfe3f5)}
.member .badge{position:absolute;right:10px;top:14px;width:28px;height:28px;background:var(--accent)}
.member .name{position:absolute;left:0;width:100%;top:130px;font-family:var(--serif);font-size:13px}
.member .role{position:absolute;left:20px;width:148px;top:149px;font-size:11px;line-height:15px;color:var(--accent)}

/* footer */
.footer-bg{left:0;top:3250px;width:1200px;height:545px;background:linear-gradient(180deg,#0c121a 0%,#161a1f 40%,#1a1c1f 100%)}
.footer-brand{left:0;width:1200px;top:3375px;display:flex;justify-content:center}
.footer-intro{left:0;width:1200px;top:3446px;text-align:center;font-size:11.5px;line-height:21px;color:#ddd}
.footer-rule{left:161px;top:3529px;width:878px;height:1px;background:#3a3e44}
.fcol{top:3572px;font-size:11.5px;color:#e0e0e0}
.fcol h4{font-family:var(--serif);font-weight:400;font-size:14px;color:var(--white)}
.fcol .underline{width:40px;height:2px;background:var(--accent);margin:8px 0 20px}
.fcol ul{list-style:none;line-height:19.5px}
.socials{left:161px;top:3748px;display:flex;gap:10px}
.socials span{width:28px;height:28px;background:var(--white)}
.contact-row{display:flex;align-items:flex-start;gap:14px;margin-bottom:24px;line-height:19px}
.contact-row svg{flex:none}
.copyright{left:0;top:3795px;width:1200px;height:46px;background:var(--accent);display:flex;align-items:center;justify-content:center;font-size:11.5px}
</style>
</head>
<body>

<header class="site-header abs">
  <a class="brand"><span class="brand-mark"></span>BRACKENFORD</a>
  <nav class="main-nav"><a>About</a><a>Expertise</a><a>Case Studies</a><a>Team</a><a>Contact Us</a></nav>
  <a class="btn-header">Contact Us</a>
</header>

<section class="hero abs" role="img" aria-label="Upward view of high-rise residential towers against the sky"></section>
<h1 class="hero-title abs" style="font-weight:400">WE DEVELOPS CORPORATE AND<br>PROFESSIONAL BOTH PROPERTY</h1>
<p class="hero-sub abs">Specialising in medium to high density projects, we focus on properties that provide sustained rental and capital growth and use our expertise in redevelopment and repurposing to continuously improve value.</p>
<a class="btn-quote abs">Get A Free Quote</a>
<div class="vline abs" style="left:599px;top:578px;height:170px"></div>
<div class="slider-ctrl abs">
  <span class="tri-l" style="border-right-color:#ddd"></span>
  <span class="current">02</span>
  <div class="dots"><span style="left:0"></span><span style="left:30px"></span><span style="left:60px"></span><span style="left:90px"></span><span style="left:119px"></span></div>
  <span>05</span>
  <span class="tri-r" style="border-left-color:#ddd;margin-left:20px"></span>
</div>

<h2 class="section-title abs" style="top:812px;font-weight:400">Our Expertise</h2>
<nav class="tabs abs"><span>ALL</span><span>ACQUISITIONS</span><span class="active">PLANNING AND CONSENTING</span><span>DEVELOPMENT</span><span>RENOVATION AND REPOSITIONING</span></nav>

<div class="tile abs" style="left:0;width:116px" role="img" aria-label="Glass office tower with blue overlay"></div>
<div class="tile abs" style="left:146px;width:240px" role="img" aria-label="Modern curved building with blue overlay"></div>
<div class="tile tile-photo abs" style="left:416px;width:240px" role="img" aria-label="Timber lookout tower beside bare trees"></div>
<div class="plus-btn abs"><svg width="76" height="73" viewBox="0 0 76 73"><path d="M38 26v21M27.5 36.5h21" stroke="#fff" stroke-width="2"/></svg></div>
<h3 class="exp-heading abs" style="font-weight:400">Resource Management<br>Planning And Consenting</h3>
<p class="exp-text abs">The Brackenford team is able to obtain complex development consents by working closely with the city and key stakeholders and involving local communities and interest groups. This, combined with deep local market knowledge, meticulous planning and decades of experience, results in the best possible consenting outcome for our proposed projects.</p>
<div class="pager abs" style="left:702px;top:1257px"><span><i class="tri-l"></i>PREVIOUS</span><span>NEXT<i class="tri-r"></i></span></div>

<div class="about-photo abs" role="img" aria-label="White colonial apartment building with palm trees under a clear sky"></div>
<section class="about-panel abs">
  <h2>About Us</h2>
  <p>Brackenford Group is a privately-owned commercial real estate investment company founded in Auckland in 2007. Working with a small group of long-standing private and institutional partners, the firm has successfully acquired and developed assets valued at over $1.0 billion.<br>Brackenford Group has a long track record of success in the acquisition, consenting, development, renovation and repositioning of office, tourism accommodation, residential, social housing, retail and mixed use properties within the Auckland region.</p>
  <div class="vline"></div>
  <a class="explore">Explore More <i class="tri-r"></i></a>
</section>

<div class="cases-bg abs"></div>
<h2 class="section-title abs" style="top:2120px;font-size:34px;font-weight:400">Case Studies</h2>
<div class="case-card case-1 abs" role="img" aria-label="Modern apartment building with balconies"><div class="caption"><div class="name">Ashgrove</div><div class="addr">Ashgrove, 41 Harbour Rd,<br>Auckland CBD</div></div></div>
<div class="case-card case-2 abs" role="img" aria-label="Dark office block facade"><div class="caption">The Whitmore</div></div>
<div class="case-card case-3 abs" role="img" aria-label="Suburban house under blue sky"><div class="caption">Larkfield</div></div>
<div class="case-card case-4 abs" role="img" aria-label="House at dusk under a pink sky"><div class="caption">Halden</div></div>
<div class="vline abs" style="left:599px;top:2422px;height:67px"></div>
<h3 class="case-detail-title abs" style="font-weight:400">Ashgrove</h3>
<p class="case-detail-text abs">Lorem Ipsum is simply dummy text of the printing and typesetting industry. Lorem Ipsum has been the industry's standard dummy text ever since the 1500s, when an unknown printer took a galley of type and scrambled it to make a type specimen book. It has survived not only five centuries.</p>
<div class="pager abs" style="left:523px;top:2692px"><span><i class="tri-l"></i>PREVIOUS</span><span>NEXT<i class="tri-r"></i></span></div>

<h2 class="team-title abs" style="font-weight:400">Our Team</h2>
<p class="team-text abs">Lorem Ipsum is simply dummy text of the printing and typesetting industry. Lorem Ipsum has been the industry's standard dummy text ever since the 1500s, when an unknown printer took a galley of type and scrambled it to make a type specimen book. It has survived not only five centuries</p>

<div class="member abs" style="left:431px;top:2831px"><div class="photo" role="img" aria-label="Portrait of team member"></div><span class="badge"></span><div class="name">Daniel Marsh</div><div class="role">Senior Asset and Development Manager</div></div>
<div class="member abs" style="left:641px;top:2831px"><div class="photo" role="img" aria-label="Portrait of team member"></div><span class="badge"></span><div class="name">Owen Lockridge</div><div class="role">Director</div></div>
<div class="member abs" style="left:851px;top:2831px"><div class="photo" role="img" aria-label="Portrait of team member"></div><span class="badge"></span><div class="name">Liam Prescott</div><div class="role">Director</div></div>
<div class="member abs" style="left:431px;top:3041px"><div class="photo" role="img" aria-label="Portrait of team member"></div><span class="badge"></span><div class="name">Ethan Varley</div><div class="role">Residential Portfolio Manager</div></div>
<div class="member abs" style="left:641px;top:3041px"><div class="photo" role="img" aria-label="Portrait of team member"></div><span class="badge"></span><div class="name">Clara Fennimore</div><div class="role">Commercial Property Manager</div></div>
<div class="member abs" style="left:851px;top:3041px"><div class="photo" role="img" aria-label="Portrait of team member"></div><span class="badge"></span><div class="name">Martin Hale</div><div class="role">Financial Controller</div></div>

<footer>
  <div class="footer-bg abs" role="img" aria-label="Faint night view of city buildings"></div>
  <div class="footer-brand abs"><span class="brand"><span class="brand-mark"></span>BRACKENFORD</span></div>
  <p class="footer-intro abs">Lorem Ipsum is simply dummy text of the printing and typesetting industry.<br>Lorem Ipsum has been the industry's standard dummy text.</p>
  <div class="footer-rule abs"></div>

  <div class="fcol abs" style="left:162px"><h4>Quick Links</h4><div class="underline"></div><ul><li>Home</li><li>Expertise</li><li>Case Studies</li><li>Team</li><li>Contact Us</li></ul></div>
  <div class="fcol abs" style="left:388px"><h4>Sitemap</h4><div class="underline"></div><ul><li>About Us</li><li>Terms &amp; Conditions</li><li>Projects</li><li>Policies</li><li>News</li></ul></div>
  <div class="fcol abs" style="left:613px"><h4>Expertise</h4><div class="underline"></div><ul><li>Acquisitions</li><li>Planning And Consenting</li><li>Development</li><li>Renovation And Repositioning</li><li>Leasing And Asset Management</li><li>Financial Management</li></ul></div>
  <div class="fcol abs" style="left:838px"><h4>Office Tour</h4><div class="underline"></div>
    <div class="contact-row"><svg width="18" height="18" viewBox="0 0 24 24"><path d="M6.6 10.8a15 15 0 006.6 6.6l2.2-2.2a1 1 0 011-.25 11 11 0 003.6.6 1 1 0 011 1V20a1 1 0 01-1 1A17 17 0 013 4a1 1 0 011-1h3.5a1 1 0 011 1 11 11 0 00.6 3.6 1 1 0 01-.25 1z" fill="#1b8cf2"/></svg><span>+64 9 555 0148</span></div>
    <div class="contact-row"><svg width="18" height="14" viewBox="0 0 18 14"><rect x="0.5" y="0.5" width="17" height="13" fill="#1b8cf2"/><path d="M1 1l8 7 8-7" stroke="#fff" fill="none"/></svg><span>daniel@brackenfordgroup.co.nz</span></div>
    <div class="contact-row"><svg width="16" height="22" viewBox="0 0 16 22"><path d="M8 0a8 8 0 00-8 8c0 6 8 14 8 14s8-8 8-14a8 8 0 00-8-8z" fill="#1b8cf2"/><circle cx="8" cy="8" r="3" fill="#fff"/></svg><span>Level 6, Harbour House<br>20 Quayside Lane, Auckland CBD</span></div>
  </div>

  <div class="socials abs"><span></span><span></span><span></span><span></span></div>
  <div class="copyright abs">Copyright© 2019 Brackenford. Terms &amp; Conditions | Privacy Policy.</div>
</footer>

</body>
</html>
```